Rug Cleaning Web Design Project

We need a web design for our cleaning company. We currently have a web page but are not happy with its design. We currently offer fine rug cleaning,upholstery cleaning, and residential and commercial carpet cleanning. We also offer water damage restoration. For our rug cleaning services we offer : Enzyme treatments for pet contamination and odor removal, application of stain protection that is designed for the fine textiles used in rug construction, application of treatments designed to prevent moth damage and pads designed to be used under rugs.Our current web site is harborlinewash.example. We are intrested in a design with similar information to the web page of Velmora Rug Cleaners INC. We would like to use the colors that are present in our logo that will be uploaded with this description. We would also like this new page to be linked to our other address fibertendpro.example. We would like the deign to be visually attractive but not "too busy".
Updates

Please include pictures of rugs, or people washing rugs if possible. We do not offer maid type cleaning services. We would not be interested in designs including pictures depicting that type service. Thanks for your hard work on this project.

Dale Hutchins

Industry/Entity Type

Residential

Requirements
Must have
• This page must be viewable on smart phones and tablets.

```html
<!DOCTYPE html>
<html lang="en">
<head>
<meta charset="utf-8">
<title>FiberTendPro — Harborline Cleaning, LLC</title>
<link rel="stylesheet" href="https://fonts.googleapis.com/css2?family=PT+Sans:wght@400;700&family=Roboto+Condensed:wght@300;400;700&display=swap">
<style>
  :root {
    --page-bg: #ebebea;
    --brand-blue: #1f8bd0;
    --brand-dark: #252525;
    --text-body: #5d5d5d;
    --rule: #d3d3d3;
    --footer-bg: #3a3a3a;
    --footer-panel: #4a4a4a;
    --footer-bottom: #262626;
    --footer-text: #9a9a9a;
    --footer-title: #e2e2e2;
    --ring: #ffffff;
  }
  * { box-sizing: border-box; margin: 0; padding: 0; }
  html, body { width: 1183px; height: 1200px; overflow: hidden; }
  body {
    position: relative;
    background: var(--page-bg);
    font-family: "Roboto Condensed", Arial, sans-serif;
    color: var(--text-body);
    border-top: 3px solid #777;
  }
  .abs { position: absolute; }

  /* Header */
  .search {
    left: 833px; top: 0; width: 161px; height: 23px;
    background: #8c8c8c; border-radius: 0 0 3px 3px;
    color: #d8d8d8; font: italic 9px Arial, sans-serif;
    display: flex; align-items: center; padding-left: 28px;
  }
  .search svg { position: absolute; left: 10px; top: 6px; }
  .brand { left: 190px; top: 40px; display: flex; align-items: center; gap: 10px; }
  .brand-mark { width: 38px; height: 38px; border-radius: 50%; background: var(--brand-blue); }
  .brand-name {
    font-family: "PT Sans", sans-serif; font-weight: 700; font-size: 30px; color: var(--brand-dark);
    line-height: 1;
  }
  .header-rule { left: 0; top: 94px; width: 1183px; border-top: 1px solid var(--rule); }

  .welcome { left: 190px; top: 124px; font: 700 24px "PT Sans", sans-serif; color: var(--brand-blue); }
  .nav-rule { left: 190px; top: 151px; width: 805px; border-top: 1px solid var(--rule); }
  .nav-home {
    left: 569px; top: 109px; width: 61px; height: 43px;
    background: #dcdcdc; border-radius: 5px 5px 0 0;
    border-bottom: 2px solid var(--brand-blue);
    font: 700 16px "PT Sans", sans-serif; color: var(--brand-blue);
    text-align: center; padding-top: 14px;
  }
  .nav-links {
    right: 188px; top: 125px;
    font: 700 15px "Roboto Condensed", sans-serif; color: var(--brand-blue);
    letter-spacing: -0.2px;
  }

  /* About */
  .section-title { font: 700 24px "PT Sans", sans-serif; color: var(--brand-blue); }
  .about-title { left: 190px; top: 198px; }
  .about-text { left: 190px; top: 241px; width: 363px; }
  .about-text p {
    font: 300 12.4px/14.4px "Roboto Condensed", sans-serif;
    text-align: justify; margin-bottom: 14px; color: #555;
  }
  .hero {
    left: 618px; top: 202px; width: 378px; height: 378px; border-radius: 50%;
    background: var(--ring); box-shadow: 0 1px 4px rgba(0,0,0,.15);
  }
  .hero-fill {
    position: absolute; left: 7px; top: 7px; width: 364px; height: 364px; border-radius: 50%;
    background: radial-gradient(circle at 60% 35%, #eee8dc 0%, #cfc6b6 45%, #b8b3aa 75%, #9e9a93 100%);
  }
  .hero-dots { left: 792px; top: 537px; display: flex; gap: 5px; }
  .hero-dots span { width: 12px; height: 13px; border-radius: 50%; border: 1.5px solid var(--brand-blue); background: #fff; }
  .hero-dots span.active { background: var(--brand-blue); }

  /* Services */
  .services-title { left: 191px; top: 594px; }
  .service { top: 641px; width: 176px; text-align: center; }
  .service-ring {
    width: 176px; height: 176px; border-radius: 50%; background: var(--ring);
    box-shadow: 0 1px 4px rgba(0,0,0,.15); padding: 5px;
  }
  .service-photo { width: 166px; height: 166px; border-radius: 50%; }
  .service-label {
    display: inline-block; margin-top: 6px;
    font: 300 23px "Roboto Condensed", sans-serif; color: #6d6d6d;
    border-bottom: 1px dotted #8a8a8a; line-height: 1.1;
  }

  /* Footer */
  .footer { left: 0; top: 943px; width: 1183px; height: 209px; background: var(--footer-bg); border-top: 1px solid #555; }
  .footer-bottom { left: 0; top: 1152px; width: 1183px; height: 48px; background: var(--footer-bottom); }
  .footer-panel {
    left: 195px; top: 905px; width: 189px; height: 295px;
    background: linear-gradient(#5a5a5a, var(--footer-panel) 30%, #424242);
    border-radius: 5px 5px 0 0; box-shadow: 0 0 12px rgba(0,0,0,.25);
  }
  .footer-brand { position: absolute; left: 9px; top: 22px; display: flex; align-items: center; gap: 6px; }
  .footer-brand .brand-mark { width: 26px; height: 26px; }
  .footer-brand .brand-name { font-size: 20px; color: #232323; }
  .footer-copy {
    position: absolute; left: 16px; top: 72px; width: 164px;
    font: 400 9.5px/15.5px Arial, sans-serif; color: #b8b8b8;
  }
  .footer-divider { position: absolute; left: 16px; top: 130px; width: 158px; border-top: 1px solid #5e5e5e; }
  .connect-title {
    position: absolute; left: 16px; top: 148px;
    font: 700 15px "Roboto Condensed", sans-serif; color: var(--footer-title); letter-spacing: .3px;
  }
  .connect-text { position: absolute; left: 17px; top: 174px; font: 9px Arial, sans-serif; color: #999; }
  .social { position: absolute; left: 17px; top: 199px; display: flex; gap: 6px; }
  .social span { width: 24px; height: 24px; border-radius: 50%; background: #2a2a2a; }
  .social span.active { background: #d42a22; }
  .footer-panel-bottom {
    position: absolute; left: 0; top: 247px; width: 189px; height: 48px; background: var(--footer-bottom);
    font: 400 11px "Roboto Condensed", sans-serif; color: #cfcfcf; text-align: center; padding-top: 15px;
  }

  .widget-title { top: 977px; font: 700 15px "Roboto Condensed", sans-serif; color: var(--footer-title); letter-spacing: .3px; }
  .widget-text { font: 9.8px/15.5px Arial, sans-serif; color: var(--footer-text); }
  .text-widget { left: 407px; top: 1007px; width: 178px; }
  .text-widget p { margin-bottom: 9px; }
  .blog { left: 606px; top: 1006px; width: 178px; list-style: none; }
  .blog li { padding: 7px 0 8px; border-bottom: 1px solid #4f4f4f; }
  .blog li:last-child { border-bottom: 0; }
  .gallery { left: 812px; top: 1011px; display: grid; grid-template-columns: repeat(3, 57px); column-gap: 8px; row-gap: 5px; }
  .gallery span { width: 57px; height: 52px; border: 1px solid #6a6a6a; border-radius: 2px; }
  .bottom-nav { right: 188px; top: 1170px; font: 400 11px "Roboto Condensed", sans-serif; color: #b5b5b5; }
  .bottom-nav b { color: var(--brand-blue); font-weight: 700; }
</style>
</head>
<body>

<header>
  <div class="abs search">
    <svg width="12" height="12" viewBox="0 0 12 12"><circle cx="7.5" cy="4.5" r="3.3" fill="none" stroke="#d8d8d8" stroke-width="1.4"/><line x1="5" y1="7" x2="1" y2="11" stroke="#d8d8d8" stroke-width="1.8"/></svg>
    Search...
  </div>
  <div class="abs brand">
    <span class="brand-mark"></span>
    <span class="brand-name">FiberTendPro</span>
  </div>
  <div class="abs header-rule"></div>

  <h1 class="abs welcome">Welcome to Our Website!</h1>
  <div class="abs nav-rule"></div>
  <nav>
    <div class="abs nav-home">Home</div>
    <div class="abs nav-links">Rug Washing | Water Damage | Carpet Cleaning | Contact Us</div>
  </nav>
</header>

<main>
  <h2 class="abs section-title about-title">About Us</h2>
  <div class="abs about-text">
    <p>Lorem ipsum dolor sit amet, consectetuer adipiscing elit, sed diam nonummy nibh euismod tincidunt ut laoreet dolore magna aliquam erat volutpat. Ut wisi enim ad minim veniam, quis nostrud exerci tation ullamcorper suscipit lobortis nisl ut aliquip ex ea commodo consequat. Duis autem vel eum iriure dolor in hendrerit in vulputate velit esse molestie consequat, vel illum dolore eu feugiat nulla facilisis at vero eros et accumsan et iusto odio dignissim qui blandit praesent luptatum zzril delenit augue duis dolore te feugait nulla facilisi.</p>
    <p>Nam liber tempor cum soluta nobis eleifend option congue nihil imperdiet doming id quod mazim placerat facer possim assum. Typi non habent claritatem insitam; est usus legentis in iis qui facit eorum claritatem. Investigationes demonstraverunt lectores legere me lius quod ii legunt saepius. Claritas est etiam processus dynamicus, qui sequitur mutationem consuetudium lectorum.</p>
    <p>Mirum est notare quam littera gothica, quam nunc putamus parum claram, anteposuerit litterarum formas humanitatis per seacula quarta decima et quinta decima. Eodem modo typi, qui nunc nobis videntur parum clari, fiant sollemnes in futurum.</p>
  </div>

  <div class="abs hero">
    <div class="hero-fill" role="img" aria-label="Photo of a technician cleaning a living room carpet with a wand"></div>
  </div>
  <div class="abs hero-dots"><span></span><span class="active"></span><span></span></div>

  <h2 class="abs section-title services-title">Our Services</h2>
  <div class="abs service" style="left:189px">
    <div class="service-ring"><div class="service-photo" role="img" aria-label="Photo of a rotary machine buffing a rug" style="background:radial-gradient(circle at 50% 45%,#d9d2c4,#a7857a 55%,#7a5d55)"></div></div>
    <span class="service-label">Lorem Ipsum</span>
  </div>
  <div class="abs service" style="left:398px">
    <div class="service-ring"><div class="service-photo" role="img" aria-label="Photo of a cleaning wand on grey carpet" style="background:radial-gradient(circle at 55% 40%,#a8adae,#7f8786 60%,#5f6867)"></div></div>
    <span class="service-label">Lorem Ipsum</span>
  </div>
  <div class="abs service" style="left:611px">
    <div class="service-ring"><div class="service-photo" role="img" aria-label="Photo of carpet being steam cleaned" style="background:radial-gradient(circle at 50% 45%,#b9b7b8,#8f8c90 60%,#6d6a6d)"></div></div>
    <span class="service-label">Lorem Ipsum</span>
  </div>
  <div class="abs service" style="left:819px">
    <div class="service-ring"><div class="service-photo" role="img" aria-label="Photo of a carpet cleaning tool on light carpet" style="background:radial-gradient(circle at 50% 60%,#e6e2db,#c9c4bb 55%,#8ea8ad)"></div></div>
    <span class="service-label">Lorem Ipsum</span>
  </div>
</main>

<footer>
  <div class="abs footer"></div>
  <div class="abs footer-bottom"></div>

  <div class="abs footer-panel">
    <div class="footer-brand"><span class="brand-mark"></span><span class="brand-name">FiberTendPro</span></div>
    <p class="footer-copy">Copyright © 2012 Dale All Rights Reserved. Tidewater is Free Software released under the Open Use License.</p>
    <div class="footer-divider"></div>
    <h3 class="connect-title">CONNECT WITH US</h3>
    <p class="connect-text">Lorem ipsum dolor sit amet, conse.</p>
    <div class="social"><span></span><span class="active"></span><span></span><span></span><span></span></div>
    <div class="footer-panel-bottom">FiberTend Pro, Copyright 2012</div>
  </div>

  <h3 class="abs widget-title" style="left:407px">TEXT WIDGET</h3>
  <div class="abs widget-text text-widget">
    <p>Lorem ipsum dolor sit amet, conse cte tur adipiscing elit lorem ipsum idextae.</p>
    <p>Lorem ips um dolor sit amet, consecte tur adipiscing elit lorem ipsum idextas. Lorem ipsum dolor sit amet, conse cte tur adipiscing elit lorem ipsum.</p>
  </div>

  <h3 class="abs widget-title" style="left:606px">BLOG POST</h3>
  <ul class="abs widget-text blog">
    <li>Cum sociis natoque penatibus et ma.</li>
    <li>Lorem ipsum dolor sit amet conse cte</li>
    <li>Adipiscing elit lorem ipsum idextas.</li>
    <li>Nsecte tur adipiscing elit lorem ipsum</li>
  </ul>

  <h3 class="abs widget-title" style="left:811px">PHOTO GALLERIES</h3>
  <div class="abs gallery">
    <span role="img" aria-label="Cleaning equipment photo" style="background:linear-gradient(135deg,#d9d9d9,#8a8a8a)"></span>
    <span role="img" aria-label="Carpet texture photo" style="background:linear-gradient(135deg,#bdbdbd,#9a9a9a)"></span>
    <span role="img" aria-label="Water detail photo" style="background:linear-gradient(135deg,#8fd3e0,#3fa4bb);border-bottom:2px solid #d42a22"></span>
    <span role="img" aria-label="Hose photo" style="background:linear-gradient(135deg,#e5e5e5,#9c9c9c)"></span>
    <span role="img" aria-label="Control panel photo" style="background:linear-gradient(135deg,#cfcfcf,#9e9e9e)"></span>
    <span role="img" aria-label="Cleaning tool photo" style="background:linear-gradient(135deg,#d6d6d6,#555)"></span>
  </div>

  <nav class="abs bottom-nav"><b>Home</b> | Rug Washing | Water Damage | Carpet Cleaning | Contact Us</nav>
</footer>

</body>
</html>
```